Following list to be designed:

1. A4 Letter Head

Must comprise of:
BRIGHT HARBOR and its LOGO
Address: No.41, 2F, Tarwin Plaza, Melrick Road, Upper Fenwood Gardens, Bangalore 560 017
Tel: 080 27481930
Fax: 080 27481931
Mail: query@brightharbor.example

Color of wordings to be in the lighter shade of blue and brighter shade of blue.

2. A4 Envelope

Must comprise of:
BRIGHT HARBOR and its LOGO
Tel: 080 27481930
Fax: 080 27481931

3. Postal Envelope

Must comprise of:
BRIGHT HARBOR and its LOGO
Tel: 080 27481930
Fax: 080 27481931

4. Business Card

Must comprise of:
Rohan Mehta
Managing Partner
Cell: +91 9487215043
Mail: rohanmehta@brightharbor.example
Tel: 080 27481930
Fax: 080 27481931

5. A4 Letter Head

Must comprise of:
BRIGHT HARBOR CORP. (wording) and BRIGHT HARBOR LOGO (only blue ribbon)

Blue ribbon (BRIGHT HARBOR LOGO) may be placed on Left Top Corner of the A4 Letter Head
and BRIGHT HARBOR CORP. (wording) to be placed on Right Top Corner of the A4 Letter Head

Tel: 080 27481930
Fax: 080 27481931

6. . A4 Envelope

Must comprise of:

Blue ribbon (BRIGHT HARBOR LOGO) may be placed on Left Top Corner of the A4 Envelope
and BRIGHT HARBOR CORP. (wording) to be placed on Right Top Corner of the A4 Envelope
Tel: 080 27481930
Fax: 080 27481931

Target Market(s)

Top IT/ITES Organizations

Industry/Entity Type

Real Estate Development

Font styles to use
Serif
Sans Serif

Colors
33a6d7
0792cd
85cae6

Requirements
Should not have
• Playful font and color

```html
<!DOCTYPE html>
<html lang="en">
<head>
<meta charset="utf-8">
<title>Bright Harbor Stationery</title>
<link href="https://fonts.googleapis.com/css2?family=Lato:wght@400;700&display=swap" rel="stylesheet">
<style>
:root{
  --bg:#dcdee0;
  --paper:#ffffff;
  --blue:#0792cd;
  --blue-mid:#33a6d7;
  --blue-light:#85cae6;
  --blue-deep:#3b6fa6;
  --ink:#5a5a5a;
  --rule:#d6d6d6;
  --ghost:#f3f3f3;
}
*{margin:0;padding:0;box-sizing:border-box}
html,body{width:836px;height:1200px;overflow:hidden}
body{background:var(--bg);position:relative;font-family:'Lato',sans-serif;color:var(--ink)}
.sheet{position:absolute;background:var(--paper);box-shadow:0 1px 3px rgba(0,0,0,.18);overflow:hidden}
.sheet.topline{border-top:3px solid var(--blue-mid)}
.brand{display:flex;align-items:center;gap:4px;font-weight:700;color:var(--blue);letter-spacing:.5px;white-space:nowrap}
.brand .dot{width:8px;height:8px;background:var(--blue-mid);display:block}
.brand.small{font-size:9px}
.brand.white{color:#fff}
.brand.white .dot{background:#fff}
.ghost-name{position:absolute;font-weight:700;color:var(--ghost);white-space:nowrap;letter-spacing:1px}
.addr{position:absolute;font-size:4.6px;line-height:6.2px;color:var(--ink)}
.addr b{font-weight:700;font-size:5px;color:#444}
.footer{position:absolute;left:17px;right:17px;border-top:1px solid var(--rule);padding-top:4px;display:flex;justify-content:center;gap:8px;font-size:4.4px;color:var(--ink)}
.footer span::before{content:"";display:inline-block;width:3px;height:3px;border-radius:50%;background:var(--blue-mid);margin-right:2px;vertical-align:middle}
.flap{position:absolute;left:0;top:0;width:100%;height:51px;background:linear-gradient(180deg,var(--blue-deep),var(--blue-light));clip-path:polygon(0 0,100% 0,96.5% 100%,3.5% 100%);display:flex;align-items:center;justify-content:center}
.card-blue{background:linear-gradient(180deg,#5fbde5,var(--blue-deep));display:flex;align-items:center;justify-content:center}
</style>
</head>
<body>

<!-- Letterhead, centred brand -->
<section class="sheet topline" style="left:34px;top:100px;width:342px;height:483px">
  <div class="brand small" style="position:absolute;left:0;right:0;top:22px;justify-content:center">
    <span class="dot"></span>BRIGHT HARBOR
  </div>
  <div class="ghost-name" style="left:0;right:0;top:260px;text-align:center;font-size:30px">BRIGHT HARBOR</div>
  <p class="addr" style="left:0;right:0;top:457px;text-align:center">No.41, 2F, Tarwin Plaza, Melrick Road, Upper Fenwood Gardens, Bangalore 560 017</p>
  <div class="footer" style="top:465px"><span>080 27481930</span><span>080 27481931</span><span>query@brightharbor.example</span></div>
</section>

<!-- Envelope back, brand top left -->
<section class="sheet topline" style="left:409px;top:34px;width:394px;height:170px">
  <div class="brand small" style="position:absolute;left:9px;top:28px"><span class="dot"></span>BRIGHT HARBOR</div>
  <p class="addr" style="left:9px;top:55px">No.41, 2F, Tarwin Plaza<br>Melrick Road, Upper Fenwood Gardens<br>Bangalore 560 017</p>
  <div class="ghost-name" style="left:225px;top:95px;font-size:22px">BRIGHT HARBOR</div>
</section>

<!-- Envelope flap -->
<section class="sheet" style="left:409px;top:221px;width:394px;height:171px">
  <div class="flap"><div class="brand small white"><span class="dot"></span>BRIGHT HARBOR</div></div>
  <div class="footer" style="top:156px;left:17px;right:17px"><span>080 27481930</span><span>080 27481931</span><span>query@brightharbor.example</span></div>
</section>

<!-- Small envelope, flap side -->
<section class="sheet" style="left:550px;top:458px;width:253px;height:193px">
  <div class="flap" style="height:50px;justify-content:flex-start;padding-left:120px"><div class="brand small white"><span class="dot"></span></div></div>
  <div class="footer" style="top:179px;left:17px;right:17px"><span>080 27481930</span><span>080 27481931</span><span>query@brightharbor.example</span></div>
</section>

<!-- Small envelope, front -->
<section class="sheet topline" style="left:409px;top:426px;width:253px;height:192px">
  <div class="brand small" style="position:absolute;left:9px;top:38px"><span class="dot"></span>BRIGHT HARBOR</div>
  <p class="addr" style="left:9px;top:56px">No.41, 2F, Tarwin Plaza<br>Melrick Road, Upper Fenwood Gardens<br>Bangalore 560 017</p>
  <div class="ghost-name" style="left:85px;top:120px;font-size:22px">BRIGHT HARBOR</div>
</section>

<!-- Business card, front -->
<section class="sheet" style="left:456px;top:685px;width:139px;height:90px">
  <div class="brand" style="position:absolute;right:6px;top:24px;font-size:7px"><span class="dot" style="width:6px;height:6px"></span>BRIGHT HARBOR</div>
  <p style="position:absolute;left:6px;top:47px;font-size:5.6px;font-weight:700;color:var(--blue)">ROHAN MEHTA</p>
  <p style="position:absolute;left:6px;top:54px;font-size:3.8px;color:var(--ink)">MANAGING PARTNER</p>
  <div style="position:absolute;left:6px;right:6px;top:60px;border-top:1px solid var(--rule)"></div>
  <p class="addr" style="left:6px;top:63px;font-size:3.8px;line-height:5px">080 27481930<br>080 27481931<br>+91 9487215043<br>rohanmehta@brightharbor.example</p>
  <p class="addr" style="right:6px;top:63px;font-size:3.8px;line-height:5px;text-align:right">No.41, 2F, Tarwin Plaza<br>Melrick Road<br>Upper Fenwood Gardens<br>Bangalore 560 017</p>
</section>

<!-- Business card, back -->
<section class="sheet card-blue" style="left:616px;top:685px;width:139px;height:90px">
  <div class="brand white" style="font-size:9px"><span class="dot"></span>BRIGHT HARBOR</div>
</section>

<!-- Letterhead, brand left / corp right -->
<section class="sheet topline" style="left:34px;top:617px;width:342px;height:483px">
  <div class="brand small" style="position:absolute;left:17px;top:22px"><span class="dot"></span>BRIGHT HARBOR</div>
  <p class="addr" style="left:253px;top:14px"><b>BRIGHT HARBOR CORP.</b><br>No.41, 2F, Tarwin Plaza<br>Melrick Road, Upper Fenwood Gardens<br>Bangalore 560 017</p>
  <div class="ghost-name" style="left:0;right:0;top:260px;text-align:center;font-size:30px">BRIGHT HARBOR</div>
  <div class="footer" style="top:465px"><span>080 27481930</span><span>080 27481931</span><span>query@brightharbor.example</span></div>
</section>

<!-- Envelope, brand left with corp wording -->
<section class="sheet topline" style="left:409px;top:808px;width:394px;height:171px">
  <div class="brand small" style="position:absolute;left:9px;top:14px"><span class="dot"></span></div>
  <p class="addr" style="left:47px;top:10px"><b>BRIGHT HARBOR CORP.</b><br>No.41, 2F, Tarwin Plaza<br>Melrick Road, Upper Fenwood Gardens<br>Bangalore 560 017</p>
  <div class="ghost-name" style="left:225px;top:100px;font-size:22px">BRIGHT HARBOR</div>
</section>

<!-- Envelope flap -->
<section class="sheet" style="left:409px;top:995px;width:394px;height:171px">
  <div class="flap"><div class="brand small white"><span class="dot"></span>BRIGHT HARBOR</div></div>
  <div class="footer" style="top:156px;left:17px;right:17px"><span>080 27481930</span><span>080 27481931</span><span>query@brightharbor.example</span></div>
</section>

</body>
</html>
```